Electrician Company Website Design

I am looking to get a website designed only. I do not need it converted ot html. I simply need the design in a psd format. I have my own team for the conversion. The website is for an electrician company called Bramblecourt electric. I have created a txt document with the project parameters and specifics. I have also uploaded their logo in all avaible formats. It's a zip file.

Number of Pages Required

1 page

```html
<!DOCTYPE html>
<html lang="en">
<head>
<meta charset="utf-8">
<title>Bramblecourt Electric</title>
<link href="https://fonts.googleapis.com/css2?family=Raleway:wght@400;500&display=swap" rel="stylesheet">
<style>
:root{
  --ink:#111111;
  --paper:#ffffff;
  --night:#000000;
  --accent:#0a6ab8;
  --field:#ffffff;
  --placeholder:#9a9a9a;
  --photo-warm:#8e8a84;
  --photo-cool:#5f6f7a;
  --photo-light:#b9b6b2;
  --map:#7c9a82;
  --map-line:#9aa39c;
}
*{box-sizing:border-box;margin:0;padding:0}
html,body{width:1200px;height:2347px;overflow:hidden;background:var(--paper)}
body{position:relative;font-family:'Raleway',sans-serif;color:var(--ink)}
.abs{position:absolute}
.gallery-title{left:0;width:1200px;top:48px;text-align:center;font-size:37px;font-weight:500;letter-spacing:.5px}
.gallery-lead{left:340px;width:520px;top:104px;text-align:center;font-size:15.5px;line-height:23px}
.photo{position:absolute}
.photo-lab{left:0;top:224px;width:383px;height:254px;background:linear-gradient(135deg,var(--photo-cool),var(--photo-light) 60%,var(--photo-warm))}
.photo-bench{left:818px;top:548px;width:382px;height:255px;background:linear-gradient(120deg,#3d4a5c,#6f8a6c 55%,#a7aca5)}
.photo-desk{left:0;top:874px;width:383px;height:254px;background:linear-gradient(110deg,#cfd1d2,#9aa0a4 50%,#7a4a34)}
.feature{position:absolute;width:570px}
.feature h2{font-size:24px;font-weight:500;margin-bottom:10px}
.feature p{font-size:15.5px;line-height:22.6px}
.feature-left{left:437px;top:255px}
.feature-right{left:192px;top:573px;text-align:right}
.feature-left.third{top:905px}
.contact{left:0;top:1191px;width:1200px;height:699px;background:var(--night);color:var(--paper)}
.contact-title{left:0;width:1200px;top:70px;text-align:center;font-size:39px;font-weight:500;letter-spacing:1px}
.form-title{left:87px;top:182px;font-size:25px;font-weight:500}
.form-lead{left:88px;top:227px;font-size:15.5px}
.input{position:absolute;left:87px;width:500px;background:var(--field);color:var(--placeholder);font-size:15.5px;padding:10px 10px}
.input-title{top:278px;height:42px}
.input-message{top:347px;height:111px}
.input-email{top:484px;height:42px}
.send{left:480px;top:553px;width:107px;height:34px;background:var(--accent);border-radius:4px;text-align:center;line-height:34px;font-size:15.5px;color:var(--paper)}
.social{left:86px;top:569px;display:flex;gap:22px}
.social span{width:16px;height:16px;border:2px solid var(--paper);border-radius:50%}
.brand{left:690px;top:186px;width:255px;text-align:center;font-size:17px;font-weight:500;display:flex;align-items:center;justify-content:center;gap:8px}
.brand i{width:14px;height:14px;background:var(--paper);border-radius:50%;display:inline-block}
.info-label{left:700px;font-size:15.5px}
.icon-box{position:absolute;left:700px;width:41px;height:39px;background:var(--paper);border-radius:3px;display:flex;align-items:center;justify-content:center}
.info-text{left:762px;font-size:15.5px;line-height:19px}
.divider{left:0;top:1890px;width:1200px;height:3px;background:var(--map-line)}
.map{left:0;top:1893px;width:1200px;height:454px;background:linear-gradient(160deg,#86a18a,var(--map) 50%,#6f8f76)}
</style>
</head>
<body>
  <h1 class="abs gallery-title">Explore Our Gallery</h1>
  <p class="abs gallery-lead">Lorem ipsum dolor sit amet, consetetur sadipscing elitr, sed diam nonumy eirmod tempor invidunt ut labore et dolore magna</p>

  <div class="photo photo-lab" role="img" aria-label="Photo of three engineers working around a laptop in a lab"></div>
  <section class="feature feature-left">
    <h2>Gallery</h2>
    <p>Lorem ipsum dolor sit amet, consetetur sadipscing elitr, sed diam nonumy eirmod tempor invidunt ut labore et dolore magna aliquyam erat, sed diam voluptua. At vero eos et accusam et justo duo dolores et ea rebum. &nbsp;&nbsp;&nbsp;&nbsp;clita kasd gubergren, no sea takimata sanctus est Lorem ipsum dolor sit amet. Lorem ipsum dolor sit amet, consetetur sadipscing elitr, sed diam nonumy eirmod tempor invidunt ut labore et dolore magna aliquyam erat, sed diam</p>
  </section>

  <section class="feature feature-right">
    <h2>Gallery</h2>
    <p>Lorem ipsum dolor sit amet, consetetur sadipscing elitr, sed diam nonumy eirmod tempor invidunt ut labore et dolore magna aliquyam erat, sed diam voluptua. At vero eos et accusam et justo duo dolores et ea rebum. clita kasd gubergren, no sea takimata sanctus est Lorem ipsum dolor sit amet. Lorem ipsum dolor sit amet, consetetur sadipscing elitr, sed diam nonumy eirmod tempor invidunt ut labore et dolore magna aliquyam erat,</p>
  </section>
  <div class="photo photo-bench" role="img" aria-label="Photo of a technician inspecting wiring on a workbench"></div>

  <div class="photo photo-desk" role="img" aria-label="Photo of a developer working at a desk with monitors"></div>
  <section class="feature feature-left third">
    <h2>Gallery</h2>
    <p>Lorem ipsum dolor sit amet, consetetur sadipscing elitr, sed diam nonumy eirmod tempor invidunt ut labore et dolore magna aliquyam erat, sed diam voluptua. At vero eos et accusam et justo duo dolores et ea rebum. &nbsp;&nbsp;&nbsp;&nbsp;clita kasd gubergren, no sea takimata sanctus est Lorem ipsum dolor sit amet. Lorem ipsum dolor sit amet, consetetur sadipscing elitr, sed diam nonumy eirmod tempor invidunt ut labore et dolore magna aliquyam erat, sed diam</p>
  </section>

  <section class="abs contact">
    <h2 class="abs contact-title">Contact Us</h2>
    <h3 class="abs form-title">Contact Form</h3>
    <p class="abs form-lead">Your message goes here</p>
    <div class="input input-title">Title</div>
    <div class="input input-message">Your text message</div>
    <div class="input input-email">somename@example.com</div>
    <div class="abs social"><span></span><span></span><span></span></div>
    <div class="abs send">Send</div>

    <div class="abs brand"><i></i>Bramblecourt Electric</div>

    <p class="abs info-label" style="top:273px">Phone number for contact info:</p>
    <div class="icon-box" style="top:312px">
      <svg width="26" height="26" viewBox="0 0 24 24"><path d="M6.6 10.8a15.1 15.1 0 0 0 6.6 6.6l2.2-2.2c.3-.3.7-.4 1-.2 1.1.4 2.3.6 3.6.6.6 0 1 .4 1 1V20c0 .6-.4 1-1 1A17 17 0 0 1 3 4c0-.6.4-1 1-1h3.5c.6 0 1 .4 1 1 0 1.3.2 2.5.6 3.6.1.3 0 .7-.2 1z" fill="#000"/></svg>
    </div>
    <p class="abs info-text" style="top:322px">555 013 4827</p>

    <p class="abs info-label" style="top:380px">Address</p>
    <div class="icon-box" style="top:418px">
      <svg width="24" height="30" viewBox="0 0 24 30"><path d="M12 1C6.5 1 2 5.4 2 10.8 2 18 12 29 12 29s10-11 10-18.2C22 5.4 17.5 1 12 1z" fill="#000"/><circle cx="12" cy="11" r="4" fill="#fff"/></svg>
    </div>
    <p class="abs info-text" style="top:419px">4120 Alder Run Rd Fenwick,<br>MN 55999</p>
  </section>

  <div class="abs divider"></div>
  <div class="abs map" role="img" aria-label="Map showing the company location and surrounding towns"></div>
</body>
</html>
```